Business Card Design Project : Tidewell Press

In preparation for market launch, Whistler's Tidewell Press require the development of a business card. Tidewell Press is a Community online publishing web portal. We provide the the city of Whistler located in B.C. (Canada) business directories, News, Classified ads, News, Events and blogs etc.

The main focus of the brand is to help local businesses to corporate with their online advertisement and marketing. Meeting our clients face to face is a must (B2B).

Target Market(s)

The target market is B2B customers. Business Owners to Marketing, advertising Managers

Industry/Entity Type

Business

Requirements
Must have
• - The business card will be two sided.
the BACK side will have our logo which consist of (icon, url,slogan) submited. The logo will be middle and centred.

The FRONT side should have company details:

Company Legal Name: FERNDALE TIDEWELL PRESS

Owen Marsk
Director of Sales & Marketing

www.ferndaletidewell.biz
owen@ferndaletidewell.biz

Phone: 555 014 3826
#2817 - 562 E. Harlow Ave.
Vancouver, B.C. K7P2R4 Canada
Nice to have
• - For the "FRONT" side of our business card. You can separate or re-arrange with our logo components (icon, logo,slogan). It does not have to be together.

Also our company legal name is rather long so arrange or organize the name in a way to make it shorter. Your experience and creativity will have to come in play.
Should not have
• should not have other colors beside logo color and black text (2 colors). Also nothing Three dimensional

```html
<!DOCTYPE html>
<html lang="en">
<head>
<meta charset="utf-8">
<title>Ferndale Tidewell Press — Business Card Concepts</title>
<link rel="stylesheet" href="https://fonts.googleapis.com/css2?family=Questrial&display=swap">
<style>
  :root {
    --brand-blue: #0d7ad3;
    --ink: #1b1b1b;
    --soft-grey: #e4e4e4;
    --paper: #ffffff;
    --muted: #5a5a5a;
    --shadow: rgba(0, 0, 0, 0.55);
  }
  * { box-sizing: border-box; margin: 0; padding: 0; }
  html, body {
    width: 1200px; height: 988px; overflow: hidden;
    background: var(--paper);
    font-family: "Questrial", "Helvetica Neue", Arial, sans-serif;
  }
  .sheet { position: relative; width: 1200px; height: 988px; }

  .card {
    position: absolute; overflow: hidden;
    border-radius: 18px;
    box-shadow: 7px 7px 7px var(--shadow);
    background: var(--paper);
  }
  .card--blue { background: var(--brand-blue); }
  .card__bg { position: absolute; inset: 0; width: 100%; height: 100%; }
  .card > *:not(.card__bg) { position: absolute; }

  .front-business   { left: 36px;  top: 24px;  width: 520px; height: 276px; }
  .back-blue        { left: 640px; top: 24px;  width: 516px; height: 286px; }
  .back-white       { left: 36px;  top: 336px; width: 514px; height: 280px; }
  .front-blue       { left: 640px; top: 336px; width: 516px; height: 284px; }
  .back-blue-oval   { left: 50px;  top: 670px; width: 510px; height: 286px; }
  .front-grey       { left: 630px; top: 670px; width: 510px; height: 286px; }

  /* wordmark */
  .wordmark { display: flex; align-items: center; gap: 12px; white-space: nowrap; }
  .wordmark__dot { border-radius: 50%; flex: none; }
  .wordmark__name { text-transform: uppercase; letter-spacing: 0.06em; }
  .wordmark--centered { left: 0; right: 0; justify-content: center; }

  .slogan { white-space: nowrap; }
  .url { white-space: nowrap; letter-spacing: 0.04em; }
  .url--bold { font-size: 19px; color: var(--ink); letter-spacing: 0.08em; }
  .centered { left: 0; right: 0; text-align: center; }

  .contact { line-height: 1.55; }
  .contact__name { font-size: 22px; letter-spacing: 0.03em; }
  .contact__title { font-size: 12px; margin-top: 4px; }
  .contact__email { font-size: 10px; margin-top: 12px; }
  .contact__lines { font-size: 10px; margin-top: 14px; line-height: 1.5; }

  .on-white { color: var(--muted); }
  .on-blue { color: var(--paper); }
</style>
</head>
<body>
<main class="sheet">

  <!-- Front: white card with blue sweep -->
  <section class="card front-business">
    <svg class="card__bg" viewBox="0 0 520 276" preserveAspectRatio="none" aria-hidden="true">
      <path d="M0 0 H520 V50 C400 68 220 108 0 132 Z" fill="var(--brand-blue)"/>
    </svg>
    <div class="wordmark" style="left:22px; top:22px;">
      <span class="wordmark__dot" style="width:26px;height:26px;background:var(--paper);"></span>
      <span class="wordmark__name on-blue" style="font-size:15px;">Ferndale Tidewell Press</span>
    </div>
    <p class="slogan on-blue" style="left:60px; top:56px; font-size:11px;">your information getaway</p>
    <p class="url on-white" style="left:22px; top:204px; font-size:12px;">www.ferndaletidewell.biz</p>
    <div class="contact on-white" style="left:296px; top:136px;">
      <p class="contact__name">Owen Marsk</p>
      <p class="contact__title">Director of Sales &amp; Marketing</p>
      <p class="contact__email">owen@ferndaletidewell.biz</p>
      <p class="contact__lines">Phone: 555 014 3826<br>#2817 - 562 E. Harlow Ave.<br>Vancouver, B.C. K7P2R4 Canada</p>
    </div>
  </section>

  <!-- Back: solid blue -->
  <section class="card card--blue back-blue">
    <div class="wordmark wordmark--centered" style="top:84px;">
      <span class="wordmark__dot" style="width:48px;height:48px;background:var(--paper);"></span>
      <span class="wordmark__name on-blue" style="font-size:26px;">Ferndale Tidewell Press</span>
    </div>
    <p class="slogan centered" style="top:190px; font-size:20px; color:var(--ink);">your information getaway</p>
    <p class="url url--bold centered" style="top:236px;">www.ferndaletidewell.biz</p>
  </section>

  <!-- Back: white -->
  <section class="card back-white">
    <div class="wordmark wordmark--centered" style="top:118px;">
      <span class="wordmark__dot" style="width:48px;height:48px;background:var(--brand-blue);"></span>
      <span class="wordmark__name" style="font-size:26px;color:var(--brand-blue);">Ferndale Tidewell Press</span>
    </div>
    <p class="slogan centered" style="top:196px; font-size:20px; color:var(--brand-blue);">your information getaway</p>
    <p class="url url--bold centered" style="top:238px;">www.ferndaletidewell.biz</p>
  </section>

  <!-- Front: blue card with white header -->
  <section class="card card--blue front-blue">
    <svg class="card__bg" viewBox="0 0 516 284" preserveAspectRatio="none" aria-hidden="true">
      <path d="M0 0 H516 V70 C380 64 180 80 0 112 Z" fill="var(--paper)"/>
    </svg>
    <div class="wordmark" style="left:14px; top:18px;">
      <span class="wordmark__dot" style="width:26px;height:26px;background:var(--brand-blue);"></span>
      <span class="wordmark__name" style="font-size:15px;color:var(--brand-blue);">Ferndale Tidewell Press</span>
    </div>
    <p class="slogan" style="left:52px; top:52px; font-size:11px; color:var(--ink);">your information getaway</p>
    <p class="url on-blue" style="left:10px; top:182px; font-size:12px;">www.ferndaletidewell.biz</p>
    <div class="contact on-blue" style="left:272px; top:110px;">
      <p class="contact__name">Owen Marsk</p>
      <p class="contact__title">Director of Sales &amp; Marketing</p>
      <p class="contact__email">owen@ferndaletidewell.biz</p>
      <p class="contact__lines">Phone: 555 014 3826<br>#2817 - 562 E. Harlow Ave.<br>Vancouver, B.C. K7P2R4 Canada</p>
    </div>
  </section>

  <!-- Back: blue with light oval -->
  <section class="card card--blue back-blue-oval">
    <svg class="card__bg" viewBox="0 0 510 286" preserveAspectRatio="none" aria-hidden="true">
      <ellipse cx="255" cy="300" rx="210" ry="52" fill="var(--soft-grey)"/>
    </svg>
    <div class="wordmark wordmark--centered" style="top:104px;">
      <span class="wordmark__dot" style="width:44px;height:44px;background:var(--paper);"></span>
      <span class="wordmark__name on-blue" style="font-size:25px;">Ferndale Tidewell Press</span>
    </div>
    <p class="slogan centered on-blue" style="top:196px; font-size:20px;">your information getaway</p>
    <p class="url centered" style="top:256px; font-size:19px; letter-spacing:0.08em; color:var(--brand-blue);">www.ferndaletidewell.biz</p>
  </section>

  <!-- Front: grey header, blue body -->
  <section class="card front-grey" style="background:var(--brand-blue);">
    <svg class="card__bg" viewBox="0 0 510 286" preserveAspectRatio="none" aria-hidden="true">
      <path d="M0 0 H510 V84 C380 80 200 96 0 122 Z" fill="var(--soft-grey)"/>
    </svg>
    <div class="wordmark" style="left:14px; top:22px;">
      <span class="wordmark__dot" style="width:26px;height:26px;background:var(--brand-blue);"></span>
      <span class="wordmark__name" style="font-size:15px;color:var(--brand-blue);">Ferndale Tidewell Press</span>
    </div>
    <p class="slogan" style="left:52px; top:56px; font-size:11px; color:var(--ink);">your information getaway</p>
    <p class="url on-blue" style="left:14px; top:160px; font-size:12px;">www.ferndaletidewell.biz</p>
    <div class="contact on-blue" style="left:262px; top:112px;">
      <p class="contact__name">Owen Marsk</p>
      <p class="contact__title">Director of Sales &amp; Marketing</p>
      <p class="contact__email">owen@ferndaletidewell.biz</p>
      <p class="contact__lines">Phone: 555 014 3826<br>#2817 - 562 E. Harlow Ave.<br>Vancouver, B.C. K7P2R4 Canada</p>
    </div>
  </section>

</main>
</body>
</html>
```